Modern business card for triathlon training business in Australia

We need a business card design for our triathlon training company.

Pace with Us Fitness is an Australian business, owned by women, run for women. Pace with Us Fitness helps women prepare or improve triathlon skills and confidence through triathlon camps completely designed for women.

Our camps focus on preparing women both physically and mentally for their next (or first!) triathlon.

You can see our website www.pacewithusfitness.com.au for more info about our business and our style.

We've attached two of our logos and are happy to consider a design that utilised either colour scheme with the teal colour being our 'feature' colour. We don't want overly feminine cards but rather cards that are professional and neat. If the inclusion of any pictures/art is warranted, this should be focused on our swim/ride/run theme and in that specific order (swim/ride/run).

The business card needs to be a printable design and the contact details will need to change for our two employees.

Target Market(s)

Female clients and partners/vendors/sponsors that we work with in the triathlon industry

Industry/Entity Type

Fitness

Contact Information for Business Card

Pace with Us Fitness (business name)
Nina Carver
Business Director
Mobile: 0438 916 207
Email: nina@pacewithusfitness.com.au
www.pacewithusfitness.com.au

Second business card:
Pace with Us Fitness
Bel Stray
Coaching Director
Mobile: 0459 260 718
Email: bel@pacewithusfitness.com.au

Font styles to use
Serif
Sans Serif

Requirements
Must have
• Core contact details above, our logo and be a printable design
Should not have
• Pink
• Cursive/script fonts

```html
<!DOCTYPE html>
<html lang="en">
<head>
<meta charset="utf-8">
<title>Pace with Us Fitness – Business Card</title>
<link rel="stylesheet" href="https://fonts.googleapis.com/css2?family=Open+Sans:wght@400;600;700&display=swap">
<style>
  :root {
    --page-bg: #e9e7e3;
    --card-black: #0d0e10;
    --card-charcoal: #24272b;
    --teal: #3fd0de;
    --teal-deep: #22b3c3;
    --silver: #b9bcc0;
    --white: #ffffff;
    --muted: #c9ccd0;
  }
  * { box-sizing: border-box; margin: 0; padding: 0; }
  html, body {
    width: 1200px;
    height: 1022px;
    overflow: hidden;
    background: var(--page-bg);
    font-family: "Open Sans", Arial, sans-serif;
  }
  .card {
    position: absolute;
    left: 120px;
    top: 237px;
    width: 960px;
    height: 548px;
    border-radius: 6px;
    overflow: hidden;
    background: linear-gradient(160deg, var(--card-charcoal) 0%, var(--card-black) 55%);
    box-shadow: 0 18px 40px rgba(0,0,0,0.28);
  }
  .card__wave {
    position: absolute;
    inset: 0;
    width: 100%;
    height: 100%;
  }
  .brand {
    position: absolute;
    left: 70px;
    top: 318px;
    display: flex;
    align-items: center;
    gap: 16px;
  }
  .brand__dot {
    width: 30px;
    height: 30px;
    border-radius: 50%;
    background: var(--teal);
  }
  .brand__name {
    color: var(--teal);
    font-size: 36px;
    font-weight: 600;
    letter-spacing: 0.5px;
  }
  .contact {
    position: absolute;
    right: 110px;
    top: 44px;
    text-align: right;
    color: var(--white);
  }
  .contact__name {
    font-size: 42px;
    font-weight: 700;
    line-height: 1.05;
  }
  .contact__title {
    font-size: 22px;
    font-weight: 600;
    color: var(--muted);
    margin-top: 2px;
  }
  .contact__lines {
    margin-top: 30px;
    font-size: 22px;
    font-weight: 400;
    line-height: 1.5;
  }
  .contact__phone { margin-bottom: 22px; }
  .icons {
    position: absolute;
    right: 48px;
    top: 56px;
    display: flex;
    flex-direction: column;
    gap: 14px;
  }
  .icons svg {
    width: 26px;
    height: 26px;
    stroke: var(--muted);
    fill: none;
    stroke-width: 1.8;
  }
</style>
</head>
<body>
  <div class="card">
    <svg class="card__wave" viewBox="0 0 960 548" preserveAspectRatio="none" aria-hidden="true">
      <path d="M300 548 C520 450 700 390 960 330 L960 548 Z" fill="var(--silver)"/>
      <path d="M355 548 C560 465 720 410 960 368 L960 548 Z" fill="var(--white)"/>
      <path d="M372 548 C575 472 730 420 960 380 L960 548 Z" fill="var(--teal)"/>
      <path d="M540 548 C700 490 820 455 960 440 L960 548 Z" fill="var(--teal-deep)" opacity="0.35"/>
    </svg>

    <div class="brand">
      <span class="brand__dot"></span>
      <span class="brand__name">Pace with Us Fitness</span>
    </div>

    <div class="contact">
      <p class="contact__name">Nina Carver</p>
      <p class="contact__title">Business Director</p>
      <div class="contact__lines">
        <p class="contact__phone">0438 916 207</p>
        <p class="contact__web">www.pacewithusfitness.com.au</p>
        <p class="contact__email">nina@pacewithusfitness.com.au</p>
      </div>
    </div>

    <div class="icons">
      <svg viewBox="0 0 24 24" aria-label="Mobile"><rect x="7" y="3" width="10" height="18" rx="2"/><line x1="11" y1="18" x2="13" y2="18"/></svg>
      <svg viewBox="0 0 24 24" aria-label="Web"><circle cx="12" cy="12" r="9"/><ellipse cx="12" cy="12" rx="4" ry="9"/><line x1="3" y1="12" x2="21" y2="12"/></svg>
      <svg viewBox="0 0 24 24" aria-label="Email"><rect x="3" y="6" width="18" height="12" rx="1"/><polyline points="3,6 12,13 21,6"/></svg>
    </div>
  </div>
</body>
</html>
```